Kestravo - Home Loans

We need a DL sized (214mm x 103mm) flyer to be designed for our mortgage broking arm of the business. We want something that prospective clients can pick up and remind them to review their current interest rates, potentially save thousands of dollars over the life of the loan. Or for those who are currently in the market for a new property - just to let them know we can potentially compare over 30 lenders to identify the right loan for them.

Designs to be in shades of green - refer to our website: www.kestravo.com.au/
Logos attached also.

Industry/Entity Type

Loan

```html
<!DOCTYPE html>
<html lang="en">
<head>
<meta charset="utf-8">
<title>Kestravo Home Loans Flyer</title>
<link rel="stylesheet" href="https://fonts.googleapis.com/css2?family=Arimo:wght@400;700&display=swap">
<style>
  :root {
    --backdrop: #97989b;
    --paper: #ffffff;
    --leaf-green: #8cc63f;
    --lime: #d7df23;
    --ink: #1a1a1a;
    --shadow-band: #2b2b2b;
    --tone-olive: #9a9a45;
    --tone-hair: #4a3f38;
    --tone-shirt: #5f6366;
    --tone-wall: #cfc6b4;
    --tone-sky: #eeeae2;
  }
  * { box-sizing: border-box; margin: 0; padding: 0; }
  html, body { width: 780px; height: 1200px; overflow: hidden; }
  body {
    background: var(--backdrop);
    font-family: "Arimo", Arial, sans-serif;
    position: relative;
  }
  .flyer {
    position: absolute;
    left: 150px;
    top: 113px;
    width: 483px;
    height: 1008px;
    background: var(--paper);
    overflow: hidden;
  }
  .flyer-art {
    position: absolute;
    left: 0; top: 0;
    width: 483px;
    height: 700px;
  }
  .hex-label {
    position: absolute;
    color: var(--paper);
    font-weight: 700;
    text-align: center;
    line-height: 1.02;
    text-transform: uppercase;
  }
  .hex-label--rate { left: 97px; width: 200px; top: 334px; font-size: 32px; }
  .hex-label--loan { left: 338px; width: 140px; top: 316px; font-size: 32px; }
  .hex-label--call { left: 207px; width: 200px; top: 522px; font-size: 54px; line-height: 0.95; }

  .brand {
    position: absolute;
    left: 0; width: 100%;
    top: 786px;
    display: flex;
    justify-content: center;
    align-items: center;
    gap: 14px;
  }
  .brand-mark {
    width: 40px; height: 40px;
    background: var(--leaf-green);
  }
  .brand-name {
    font-size: 44px;
    font-weight: 400;
    color: var(--ink);
    letter-spacing: 1px;
    text-transform: uppercase;
  }

  .phone-band {
    position: absolute;
    left: 0; top: 878px;
    width: 100%; height: 84px;
    background: var(--leaf-green);
    display: flex;
    justify-content: center;
    align-items: center;
    gap: 18px;
  }
  .phone-band svg { width: 26px; height: 34px; }
  .phone-number {
    color: var(--paper);
    font-size: 44px;
    font-weight: 700;
    letter-spacing: 1px;
  }
  .web-band {
    position: absolute;
    left: 0; top: 962px;
    width: 100%; height: 46px;
    background: #000;
    display: flex;
    justify-content: center;
    align-items: center;
  }
  .web-address {
    color: var(--lime);
    font-size: 28px;
    font-weight: 700;
  }
</style>
</head>
<body>
  <main class="flyer">
    <svg class="flyer-art" viewBox="0 0 483 700">
      <defs>
        <linearGradient id="photoTone" x1="0" y1="1" x2="1" y2="0">
          <stop offset="0" stop-color="var(--tone-olive)"/>
          <stop offset="0.25" stop-color="var(--tone-hair)"/>
          <stop offset="0.5" stop-color="var(--tone-shirt)"/>
          <stop offset="0.78" stop-color="var(--tone-wall)"/>
          <stop offset="1" stop-color="var(--tone-sky)"/>
        </linearGradient>
      </defs>
      <polygon class="hero-photo" role="img" aria-label="Photo of a couple embracing, seen from behind, looking up at a new two-storey home"
               points="0,0 483,0 483,420 205,520 0,420" fill="url(#photoTone)"/>
      <polygon class="shadow-band" points="0,420 205,520 205,542 0,440" fill="var(--shadow-band)"/>

      <polygon class="hex hex--rate" points="197,271 297,327 297,439 197,495 97,439 97,327"
               fill="var(--leaf-green)" stroke="var(--paper)" stroke-width="6"/>
      <polygon class="hex hex--loan" points="405,266 505,322 505,434 405,490 305,434 305,322"
               fill="var(--leaf-green)" stroke="var(--paper)" stroke-width="6"/>
      <polygon class="hex hex--call" points="305,459 403,514 403,625 305,680 207,625 207,514"
               fill="var(--lime)" stroke="var(--paper)" stroke-width="6"/>
    </svg>

    <p class="hex-label hex-label--rate">Find a<br>better<br>rate</p>
    <p class="hex-label hex-label--loan">Find<br>the<br>right<br>loan</p>
    <p class="hex-label hex-label--call">Call<br>now</p>

    <div class="brand">
      <span class="brand-mark"></span>
      <span class="brand-name">Kestravo</span>
    </div>

    <div class="phone-band">
      <svg viewBox="0 0 24 32" aria-hidden="true">
        <path d="M6 1 C3 2 1 5 1 9 C1 18 8 28 15 31 C18 32 21 31 23 28 L18 22 C17 21 15 22 14 23 C11 21 7 14 7 10 C8 9 10 9 10 7 L7 1 Z" fill="var(--paper)"/>
      </svg>
      <span class="phone-number">1300 555 274</span>
    </div>

    <div class="web-band">
      <span class="web-address">kestravo.com.au</span>
    </div>
  </main>
</body>
</html>
```